Create the design of Sitepelican (in photoshop or similar)

*edit* What we wanna see is a sketch of a first page, and then in the end 5 page designs, but the main page will be the big tasks other pages are just basically pop-ups or form. *edit*

We need a web design for our new startup Sitepelican in turn will be providing web pages to smaller business. So the purpose of the page is to clearly showcase the message in a web 3.0 fashion, good design looks but function should always be the main focus.Further more we are looking for a long term relationship with a good designer / design company that can help us design the future web sites for our customers as well.

We need you to understand web, not just design. You need to be up to date with how web looks and works, and how to make it as simple and easy to use as possible for the customer and at the same time good looking.

Please look at the PDF for full description of the project.

Colors and layout are free to choose, but we really like the kind of layout that forkglider.com has so feel free to be inspired by them.

We want all of the pages design, but the main/landing page will be the big part, the rest are small pages that will use the same design frame as the main page.

PS. We just want the design in photoshop or illustrator format, the website will then be built in page tidal by page tidal experts (let us know if you/company also possess this knowledge)

Target Market(s)

Small to medium sized business, mostly owner/entrepreneur driven companies.

Industry/Entity Type

Business

Font styles to use
Other font styles liked:
• Helvetica for the win

Requirements
Must have
• Great and simple design, a child should be able to understand the message and also enjoy reading it. Should be a funny website while still being professional, i.e. see postbadger.com for example.

```html
<!DOCTYPE html>
<html lang="en">
<head>
<meta charset="utf-8">
<title>Sitepelican – Website on subscription</title>
<link rel="stylesheet" href="https://fonts.googleapis.com/css2?family=Arimo:wght@400;700&display=swap">
<style>
:root{
  --red:#e31513;
  --red-dark:#c40f0e;
  --black:#0c0c0c;
  --ink:#1b1b1b;
  --grey-text:#7a7a7a;
  --panel:#f5f5f5;
  --panel-line:#e4e4e4;
  --subbar:#eeeeee;
  --pink:#f2cfcf;
  --cell:#dcdcdc;
  --green:#1fb83a;
  --white:#ffffff;
}
*{box-sizing:border-box;margin:0;padding:0}
html,body{width:746px;height:1200px;overflow:hidden;background:var(--white);font-family:"Arimo",Helvetica,Arial,sans-serif;color:var(--ink)}
.page{position:relative;width:746px;height:1200px;overflow:hidden}
.abs{position:absolute}

/* header */
.topbar{left:0;top:0;width:746px;height:30px;background:var(--black)}
.subbar{left:0;top:30px;width:746px;height:20px;background:var(--subbar)}
.logo-badge{left:100px;top:0;width:120px;height:62px}
.brand{left:112px;top:12px;width:96px;text-align:center;color:var(--white);font-weight:700;font-size:14px}
.brand-dot{display:inline-block;width:7px;height:7px;border-radius:50%;background:var(--red);margin-left:3px;vertical-align:1px}
.nav{left:300px;top:0;height:30px;display:flex;align-items:center}
.nav a{color:var(--white);text-decoration:none;font-size:7.5px;font-weight:700;padding:0 21px;border-left:1px solid #444;line-height:12px}
.nav a:first-child{border-left:0;color:var(--red)}
.utility{left:498px;top:34px;display:flex;align-items:center;gap:6px;font-size:7px;color:#777}
.utility .sep{width:1px;height:10px;background:#ccc}
.flag{width:16px;height:10px;display:inline-block}

/* hero */
.headline{left:0;top:92px;width:746px;text-align:center;font-size:19px;line-height:22px;color:var(--ink)}
.hero-shadow{left:100px;top:240px;width:546px;height:46px;background:radial-gradient(ellipse at center,rgba(0,0,0,.55) 0%,rgba(0,0,0,.15) 55%,rgba(0,0,0,0) 72%)}
.hero-box{left:151px;top:152px;width:443px;height:113px}
.url-input{left:165px;top:168px;width:295px;height:24px;background:var(--white);border:1px solid #bbb;font-size:12px;padding:4px 6px;color:#333}
.subscribe-btn{left:466px;top:168px;width:107px;height:23px;background:linear-gradient(#8c8c8c,#4a4a4a);color:var(--white);font-size:13px;text-align:center;line-height:23px;border:1px solid #3a3a3a}
.hero-band{left:151px;top:206px;width:443px;height:26px;background:var(--black)}
.hero-caption{left:151px;top:232px;width:443px;height:33px;background:var(--red);color:var(--white);text-align:center;font-size:19.5px;line-height:33px}

/* panels */
.panel{background:var(--panel);border:1px solid var(--panel-line)}
.about{left:100px;top:317px;width:546px;height:241px}
.about h2{position:absolute;left:26px;top:30px;font-weight:400;font-size:19px}
.about h2 span{color:var(--red);font-size:26px}
.points{position:absolute;left:26px;top:76px;list-style:none}
.points li{position:relative;padding-left:24px;font-size:9px;line-height:12px;margin-bottom:10px;width:240px}
.points li svg{position:absolute;left:0;top:1px}
.about .lorem{position:absolute;left:26px;top:136px;width:230px;font-size:7.4px;line-height:9.8px;color:var(--grey-text)}
.read-more{position:absolute;left:27px;top:196px;width:64px;height:21px;background:var(--red);color:var(--white);font-size:8.5px;text-align:center;line-height:21px;border-radius:2px}
.about-art{left:428px;top:342px;width:192px;height:192px;border-radius:50%;background:radial-gradient(circle at 50% 45%,#fbf6ea 0%,#eef3ee 55%,#dfe9e9 100%);border:2px solid #d6dede}

.cards{left:100px;top:573px;width:546px;height:255px}
.card-title{top:30px;width:200px;text-align:center;font-size:16px}
.card-photo{width:100px;height:100px;border-radius:50%;border:2px solid #d7d7d7}
.photo-money{left:96px;top:60px;background:radial-gradient(circle at 40% 45%,#cfd2c4,#6f7566 70%,#3c3f36)}
.photo-worry{left:358px;top:61px;background:radial-gradient(circle at 45% 40%,#b98a5a,#8a6a46 55%,#3d3530)}
.card-text{top:178px;width:200px;text-align:center;font-size:7.4px;line-height:10px;color:var(--ink)}
.card-divider{left:276px;top:64px;width:1px;height:160px;background:var(--panel-line)}

.calc{left:100px;top:846px;width:546px;height:278px}
.calc h2{position:absolute;left:27px;top:18px;font-weight:400;font-size:17px}
.calc-table{position:absolute;left:26px;top:52px;border-collapse:collapse;width:495px;table-layout:fixed}
.calc-table th{height:24px;font-size:8.5px;font-weight:400;color:var(--white);background:var(--black);border-right:1px solid #555}
.calc-table th.first{background:var(--red)}
.calc-table th span{color:var(--red)}
.calc-table td{text-align:center;font-size:13px;background:var(--cell);border-top:1px solid #cacaca;border-right:1px solid #e9e9e9}
.calc-table td.visitors{background:var(--pink)}
.calc-table tr.r1 td{height:44px}
.calc-table tr.r2 td{height:44px}
.calc-table tr.r3 td{height:42px}
.calc-btn{position:absolute;left:196px;top:226px;width:154px;height:32px;background:var(--red);color:var(--white);font-size:17px;text-align:center;line-height:32px}

/* footer */
.footer{left:0;top:1140px;width:746px;height:60px;background:var(--black)}
.footer-brand{left:101px;top:1162px;color:var(--white);font-weight:700;font-size:12.5px}
.footer-copy{left:182px;top:1166px;color:var(--white);font-size:6.8px}
.footer-links{right:108px;top:1168px;font-size:7px;font-weight:700;color:var(--white)}
.footer-links .active{color:var(--red)}
</style>
</head>
<body>
<div class="page">

  <header>
    <div class="abs topbar"></div>
    <div class="abs subbar"></div>
    <svg class="abs logo-badge" viewBox="0 0 120 62" aria-hidden="true">
      <polygon points="0,0 120,0 120,30 60,62 0,30" fill="#0c0c0c"/>
    </svg>
    <div class="abs brand">Sitepelican<span class="brand-dot"></span></div>
    <nav class="abs nav">
      <a href="#">Home</a><a href="#">How it work</a><a href="#">About Us</a><a href="#">FAQ</a><a href="#">Contact Us</a>
    </nav>
    <div class="abs utility">
      <svg width="12" height="9" viewBox="0 0 12 9" aria-hidden="true"><path d="M1 1h8v5H4L2 8V6H1z" fill="none" stroke="#999"/></svg>
      <span>Live chat</span><span class="sep"></span><span>Language</span>
      <svg class="flag" viewBox="0 0 16 10" role="img" aria-label="English"><rect width="16" height="10" fill="#1f3c8c"/><path d="M0 0L16 10M16 0L0 10" stroke="#fff" stroke-width="2"/><path d="M0 0L16 10M16 0L0 10" stroke="#d22" stroke-width=".8"/><rect x="6.3" width="3.4" height="10" fill="#fff"/><rect y="3.3" width="16" height="3.4" fill="#fff"/><rect x="7.1" width="1.8" height="10" fill="#d22"/><rect y="4.1" width="16" height="1.8" fill="#d22"/></svg>
      <svg class="flag" viewBox="0 0 16 10" role="img" aria-label="Swedish"><rect width="16" height="10" fill="#1a61b0"/><rect x="5" width="2" height="10" fill="#f7c600"/><rect y="4" width="16" height="2" fill="#f7c600"/></svg>
    </div>
  </header>

  <section class="hero">
    <h1 class="abs headline" style="font-weight:400">Your website on subscription autopilot with free<br>unlimited support and updates</h1>
    <div class="abs hero-shadow"></div>
    <svg class="abs hero-box" viewBox="0 0 443 113" preserveAspectRatio="none" aria-hidden="true">
      <path d="M0 4 L3 0 L6 4 L9 0 L12 4 L15 0 L18 4 L21 0 L24 4 L27 0 L30 4 L33 0 L36 4 L39 0 L42 4 L45 0 L48 4 L51 0 L54 4 L57 0 L60 4 L63 0 L66 4 L69 0 L72 4 L75 0 L78 4 L81 0 L84 4 L87 0 L90 4 L93 0 L96 4 L99 0 L102 4 L105 0 L108 4 L111 0 L114 4 L117 0 L120 4 L123 0 L126 4 L129 0 L132 4 L135 0 L138 4 L141 0 L144 4 L147 0 L150 4 L153 0 L156 4 L159 0 L162 4 L165 0 L168 4 L171 0 L174 4 L177 0 L180 4 L183 0 L186 4 L189 0 L192 4 L195 0 L198 4 L201 0 L204 4 L207 0 L210 4 L213 0 L216 4 L219 0 L222 4 L225 0 L228 4 L231 0 L234 4 L237 0 L240 4 L243 0 L246 4 L249 0 L252 4 L255 0 L258 4 L261 0 L264 4 L267 0 L270 4 L273 0 L276 4 L279 0 L282 4 L285 0 L288 4 L291 0 L294 4 L297 0 L300 4 L303 0 L306 4 L309 0 L312 4 L315 0 L318 4 L321 0 L324 4 L327 0 L330 4 L333 0 L336 4 L339 0 L342 4 L345 0 L348 4 L351 0 L354 4 L357 0 L360 4 L363 0 L366 4 L369 0 L372 4 L375 0 L378 4 L381 0 L384 4 L387 0 L390 4 L393 0 L396 4 L399 0 L402 4 L405 0 L408 4 L411 0 L414 4 L417 0 L420 4 L423 0 L426 4 L429 0 L432 4 L435 0 L438 4 L441 0 L443 4 L443 113 L0 113 Z" fill="#e31513"/>
    </svg>
    <div class="abs url-input">http\\</div>
    <div class="abs subscribe-btn">Subscripte</div>
    <div class="abs hero-band"></div>
    <div class="abs hero-caption">Subscription your website</div>
  </section>

  <section class="abs panel about">
    <h2>What is <span>sitepelican</span></h2>
    <ul class="points">
      <li><svg width="15" height="11" viewBox="0 0 15 11" aria-hidden="true"><path d="M0 0L15 5.5L0 11L4 5.5Z" fill="#e31513"/></svg>Your website on subscription autopilot with free unlimited support and updates.</li>
      <li><svg width="15" height="11" viewBox="0 0 15 11" aria-hidden="true"><path d="M0 0L15 5.5L0 11L4 5.5Z" fill="#e31513"/></svg>Delivery by professionals</li>
    </ul>
    <p class="lorem">Lorem ipsum dolor sit amet, consectetur adipiscing elit. Nam pulvinar magna vitae purus semnon ullamcorper sem dui quis ante. Duis varius accumsan risus, ac lacinia lorem hendrerit quis. Nullam egestas risus ac justo hendrerit non ullamcorper sem dui quis ante. Duis varius accumsan risus,</p>
    <div class="read-more">Read More</div>
  </section>
  <div class="abs about-art" role="img" aria-label="Illustration of web icons flowing from a cloud to pointing hands"></div>

  <section class="abs panel cards">
    <h3 class="abs card-title" style="left:46px;font-weight:400">What Does It Cast</h3>
    <h3 class="abs card-title" style="left:308px;top:28px;font-weight:400">If You Are Unhappy</h3>
    <div class="abs card-photo photo-money" role="img" aria-label="Photo of a hand holding banknotes"></div>
    <div class="abs card-photo photo-worry" role="img" aria-label="Photo of a stressed businessman at his desk"></div>
    <div class="abs card-divider"></div>
    <p class="abs card-text" style="left:46px">Lorem ipsum dolor sit amet, consectetur adipiscing elit. Nam pulvinar magna vitae purus semper condimentum. Aliquam eget tempus lorem, id porta neque. Donec ornare massa eu auctor fringilla. Praesent nunc velit, hendrerit ac euismod et, posuere et turpis.</p>
    <p class="abs card-text" style="left:308px;top:179px">Lorem ipsum dolor sit amet, consectetur adipiscing elit. Nam pulvinar magna vitae purus semper condimentum. Aliquam eget tempus lorem, id porta neque. Donec ornare massa eu auctor fringilla. Praesent nunc velit, hendrerit ac euismod et, posuere et turpis.</p>
  </section>

  <section class="abs panel calc">
    <h2>Calculation</h2>
    <table class="calc-table">
      <colgroup><col style="width:134px"><col style="width:121px"><col style="width:120px"><col style="width:120px"></colgroup>
      <tr><th class="first">Visitors Per month</th><th>Current Conversion</th><th>Improve Conversion</th><th>Average Purchase in <span>SEK</span> &#9662;</th></tr>
      <tr class="r1"><td class="visitors">10,000.00</td><td>
        <svg width="38" height="38" viewBox="0 0 38 38" role="img" aria-label="25% pie chart"><circle cx="19" cy="19" r="18" fill="#fff"/><path d="M19 19V1A18 18 0 0 1 37 19Z" fill="#1fb83a"/><text x="25" y="14" font-size="6" fill="#333" font-family="Arimo,sans-serif">25%</text><text x="11" y="30" font-size="6" fill="#333" font-family="Arimo,sans-serif">85%</text></svg>
      </td><td>85%</td><td>12 $</td></tr>
      <tr class="r2"><td class="visitors">10,000.00</td><td>
        <svg width="38" height="38" viewBox="0 0 38 38" role="img" aria-label="50% pie chart"><circle cx="19" cy="19" r="18" fill="#fff"/><path d="M19 1A18 18 0 0 1 19 37Z" fill="#1fb83a"/><text x="2" y="21" font-size="6" fill="#333" font-family="Arimo,sans-serif">50%</text><text x="21" y="21" font-size="6" fill="#333" font-family="Arimo,sans-serif">50%</text></svg>
      </td><td>50%</td><td>6 $</td></tr>
      <tr class="r3"><td class="visitors">10,000.00</td><td>
        <svg width="38" height="38" viewBox="0 0 38 38" role="img" aria-label="25% pie chart"><circle cx="19" cy="19" r="18" fill="#fff"/><path d="M19 19V1A18 18 0 0 1 37 19Z" fill="#1fb83a"/><text x="25" y="14" font-size="6" fill="#333" font-family="Arimo,sans-serif">25%</text><text x="11" y="30" font-size="6" fill="#333" font-family="Arimo,sans-serif">85%</text></svg>
      </td><td>85%</td><td>12 $</td></tr>
    </table>
    <div class="calc-btn">Calculate Now</div>
  </section>

  <footer>
    <div class="abs footer"></div>
    <div class="abs footer-brand">Sitepelican</div>
    <div class="abs footer-copy">Sitepelican © 2014 Privacy Policy</div>
    <div class="abs footer-links"><span class="active">Home</span> - How it work - About Us - FAQ - Contact Us</div>
  </footer>

</div>
</body>
</html>
```